Commercial construction contractor website.

We need a website that contains About Us, Contact info, Services, Project pictures and Industry News section

Target Market(s)

I'm building industral/flex spaces/commercial.

Industry/Entity Type

Commercial/industrial construction

Coding

Coded - Design and coding required

Number of Pages Required

5+ page

Font styles to use
Other font styles liked:
• The logo font is Microgramma Pro

Requirements
Must have
• Must have correct company name spelling: Dunmore Ridge Construction
Nice to have
• I do like to see our logo design implemented in the design
Should not have
• Please do not show big city pictures and business suit people. We are a commercial construction company

```html
<!DOCTYPE html>
<html lang="en">
<head>
<meta charset="utf-8">
<title>Dunmore Ridge Construction</title>
<link href="https://fonts.googleapis.com/css2?family=Roboto+Condensed:wght@700&family=Poppins:wght@400;500;600&display=swap" rel="stylesheet">
<style>
:root{
  --blue:#1b8fd8;
  --blue-dark:#0f5f9e;
  --navy:#0c2b4b;
  --navy-deep:#081d35;
  --ink:#1d2530;
  --text:#5d6670;
  --line:#d9dde2;
  --pale:#f2f4f6;
  --white:#ffffff;
}
*{margin:0;padding:0;box-sizing:border-box}
html,body{width:1200px;height:4092px;overflow:hidden}
body{position:relative;background:var(--white);font-family:"Poppins",sans-serif;color:var(--text);font-size:13px;line-height:1.6}
.abs{position:absolute}
.heading{font-family:"Roboto Condensed",sans-serif;font-weight:700;text-transform:uppercase;color:var(--ink);letter-spacing:.5px}
.eyebrow{font-size:11px;letter-spacing:2px;text-transform:uppercase;color:var(--ink);font-weight:500}
.btn{display:inline-block;background:var(--ink);color:var(--white);font-size:11px;font-weight:600;letter-spacing:1px;text-transform:uppercase;padding:9px 22px;clip-path:polygon(0 0,100% 0,92% 100%,0 100%)}
.photo{position:absolute}

/* header */
.site-header{position:absolute;left:0;top:0;width:1200px;height:64px;background:var(--white);box-shadow:0 2px 10px rgba(0,0,0,.06);z-index:5}
.brand{position:absolute;left:56px;top:14px;display:flex;align-items:center;gap:8px}
.brand-mark{width:30px;height:30px;background:var(--blue)}
.brand-name{font-family:"Roboto Condensed",sans-serif;font-weight:700;font-size:11px;line-height:1.2;color:var(--navy);text-transform:uppercase;width:110px}
.main-nav{position:absolute;left:460px;top:22px;display:flex;gap:26px;font-size:12px;font-weight:500;color:var(--ink)}
.main-nav .active{color:var(--blue);border-bottom:2px solid var(--blue);padding-bottom:4px}
.header-tools{position:absolute;left:925px;top:16px;display:flex;align-items:center;gap:22px}
.call{display:flex;align-items:center;gap:8px;font-size:10px;color:var(--text);line-height:1.3}
.call strong{display:block;font-size:12px;color:var(--ink)}

/* hero */
.hero{position:absolute;left:0;top:64px;width:1200px;height:540px;overflow:hidden;background:var(--navy)}
.hero-title{position:absolute;left:56px;top:150px;font-size:58px;line-height:1.02;color:var(--white)}
.hero-text{position:absolute;left:56px;top:285px;width:400px;color:#dcecf8;font-size:11px}
.hero .btn{position:absolute;left:56px;top:350px;background:rgba(255,255,255,.18);border:1px solid rgba(255,255,255,.5)}

/* about */
.about{position:absolute;left:0;top:604px;width:1200px;height:510px;background:var(--white)}
.about-copy{position:absolute;left:620px;top:80px;width:470px}
.about-copy .heading{font-size:36px;margin:4px 0 12px}
.checklist{list-style:none;margin:16px 0 20px}
.checklist li{display:flex;align-items:center;gap:12px;font-size:12px;margin-bottom:10px}
.checklist li::before{content:"";width:12px;height:12px;border:1.5px solid var(--text);border-radius:50%;flex:none}

/* services */
.services{position:absolute;left:0;top:1114px;width:1200px;height:600px}
.center{position:absolute;left:0;width:1200px;text-align:center}
.section-title{font-size:36px}
.service-card{position:absolute;top:150px;width:290px;height:370px;background:var(--white);box-shadow:0 4px 18px rgba(0,0,0,.12)}
.service-card .photo{left:12px;top:12px;width:266px;height:180px}
.service-card h3{position:absolute;left:22px;top:210px;font-size:14px;font-weight:600;color:var(--ink)}
.service-card p{position:absolute;left:22px;top:238px;width:240px;font-size:11px}
.service-card .more{position:absolute;left:22px;top:316px;font-size:10px;font-weight:600;color:var(--blue);letter-spacing:1px}
.service-card.featured{background:var(--blue)}
.service-card.featured h3,.service-card.featured p,.service-card.featured .more{color:var(--white)}

/* projects */
.projects-intro{position:absolute;left:56px;top:1780px;width:320px}
.projects-intro .heading{font-size:36px;margin:2px 0 10px}

/* contact */
.contact-copy{position:absolute;left:112px;top:2380px;width:420px}
.contact-copy .heading{font-size:34px;margin:2px 0 8px}
.field{display:block;width:290px;height:36px;border:1px solid var(--line);font-size:11px;padding:9px 12px;margin-bottom:12px;color:var(--text);background:var(--white)}
.field.focus{border-color:var(--blue)}
.field.message{height:66px}

/* news */
.news-title{top:3060px}
.news-meta{display:flex;gap:10px;align-items:center;font-size:10px;margin-bottom:6px}
.tag{background:var(--blue);color:var(--white);padding:2px 8px}
.news-card{position:absolute;background:var(--white);box-shadow:0 4px 18px rgba(0,0,0,.12);padding:18px 20px}
.news-card h4{font-size:13px;font-weight:600;color:var(--ink);line-height:1.35;margin-bottom:6px}
.news-card p{font-size:11px}

/* footer */
.site-footer{position:absolute;left:0;top:3700px;width:1200px;height:392px;background:linear-gradient(180deg,var(--navy),var(--navy-deep));color:#c8d6e4;overflow:hidden}
.footer-col h5{font-size:13px;color:var(--white);font-weight:600;margin-bottom:12px}
.footer-col ul{list-style:none;font-size:11px;line-height:2.2}
.footer-brand{position:absolute;left:450px;top:150px;width:300px;text-align:center}
.footer-brand .mark{width:54px;height:54px;border-radius:50%;background:var(--blue);margin:0 auto 12px}
.footer-brand .name{font-family:"Roboto Condensed",sans-serif;font-weight:700;font-size:22px;color:var(--white);text-transform:uppercase;line-height:1.1}
.contact-list{list-style:none;font-size:11px}
.contact-list li{display:flex;align-items:center;gap:10px;justify-content:flex-end;margin-bottom:14px}
.copyright{position:absolute;left:0;bottom:0;width:1200px;height:40px;background:var(--blue);color:var(--white);font-size:11px;text-align:center;line-height:40px}
</style>
</head>
<body>

<header class="site-header">
  <div class="brand"><span class="brand-mark"></span><span class="brand-name">Dunmore Ridge Construction</span></div>
  <nav class="main-nav">
    <span class="active">Home</span><span>About Us</span><span>Services</span><span>Project</span><span>News</span><span>Contact Us</span>
  </nav>
  <div class="header-tools">
    <svg width="16" height="16" viewBox="0 0 16 16" fill="none" stroke="#1d2530" stroke-width="2"><circle cx="7" cy="7" r="5"/><path d="M11 11l4 4"/></svg>
    <div class="call">
      <svg width="28" height="28" viewBox="0 0 28 28"><circle cx="14" cy="14" r="14" fill="#1b8fd8"/><path d="M10 8l3 3-1.5 2a8 8 0 0 0 3.5 3.5l2-1.5 3 3-2 2c-5 0-10-5-10-10z" fill="#fff"/></svg>
      <span>Call Us<strong>+1 555 014 2290</strong></span>
    </div>
  </div>
</header>

<section class="hero">
  <svg class="abs" style="left:0;top:0" width="1200" height="540" viewBox="0 0 1200 540">
    <defs>
      <linearGradient id="heroBlue" x1="0" y1="0" x2="1" y2="1"><stop offset="0" stop-color="#2aa6e8"/><stop offset="1" stop-color="#0c4f8c"/></linearGradient>
      <linearGradient id="heroPhoto" x1="0" y1="0" x2="1" y2="1"><stop offset="0" stop-color="#c9d3da"/><stop offset=".5" stop-color="#d79a52"/><stop offset="1" stop-color="#8a7a6a"/></linearGradient>
    </defs>
    <rect width="1200" height="540" fill="url(#heroBlue)"/>
    <polygon points="430,0 620,0 470,540 300,540" fill="#ffffff" opacity=".08"/>
    <polygon points="560,0 760,0 620,540 430,540" fill="#0c2b4b" opacity=".35"/>
    <polygon points="600,540 700,300 760,540" fill="#ffffff" opacity=".9"/>
    <polygon points="640,0 720,0 560,400 520,300" fill="#ffffff" opacity=".9"/>
  </svg>
  <div class="photo" role="img" aria-label="Construction workers in hard hats and safety vests reviewing plans on site" style="left:660px;top:0;width:540px;height:540px;background:linear-gradient(135deg,#c9d3da,#d79a52 55%,#7d8a95);clip-path:polygon(120px 0,540px 0,540px 540px,130px 540px,0 300px)"></div>
  <h1 class="heading hero-title">We Build Your<br>Dream</h1>
  <p class="hero-text">Lorem Ipsum is simply dummy text of the printing and typesetting industry. Lorem Ipsum has been the industry's standard dummy text ever since the 1500s.</p>
  <span class="btn">Contact Us</span>
</section>

<section class="about">
  <svg class="abs" style="left:90px;top:60px" width="430" height="390" viewBox="0 0 430 390">
    <polygon points="105,10 325,10 430,195 325,380 105,380 0,195" fill="#1b8fd8"/>
    <polygon points="90,30 300,30 400,195 300,360 90,360 20,195" fill="#0f5f9e"/>
  </svg>
  <div class="photo" role="img" aria-label="Engineer in a hard hat holding rolled building plans and talking on the phone" style="left:130px;top:95px;width:350px;height:320px;background:linear-gradient(160deg,#f1d37a,#e8ecef 45%,#5d7189);clip-path:polygon(25% 0,75% 0,100% 50%,75% 100%,25% 100%,0 50%)"></div>
  <div class="about-copy">
    <div class="eyebrow">Dunmore Ridge Construction</div>
    <h2 class="heading">About Us</h2>
    <p>Lorem Ipsum is simply dummy text of the printing and typesetting industry. Lorem Ipsum has been the industry's standard dummy text ever since the 1500s.</p>
    <ul class="checklist">
      <li>Lorem Ipsum is simply dummy text of the printing and typesetting industry.</li>
      <li>Lorem Ipsum is simply dummy text of the printing and typesetting industry.</li>
      <li>Lorem Ipsum is simply dummy text of the printing and typesetting industry.</li>
      <li>Lorem Ipsum is simply dummy text of the printing and typesetting industry.</li>
    </ul>
    <span class="btn">Contact Us</span>
  </div>
</section>

<section class="services">
  <svg class="abs" style="left:0;top:0" width="1200" height="600" viewBox="0 0 1200 600"><polygon points="0,0 1200,60 1200,600 0,600" fill="#f2f4f6"/></svg>
  <div class="center eyebrow" style="top:50px">What We Do</div>
  <h2 class="center heading section-title" style="top:68px">We Provide Service</h2>
  <article class="service-card" style="left:140px">
    <div class="photo" role="img" aria-label="Finished commercial interior with wooden shelving" style="background:linear-gradient(135deg,#efe9e0,#6b4e36)"></div>
    <h3>Commercial Design</h3>
    <p>Lorem Ipsum is simply dummy text of the printing and typesetting industry. Lorem Ipsum has.</p>
    <span class="more">LEARN MORE ›</span>
  </article>
  <article class="service-card featured" style="left:455px;top:135px;height:385px">
    <div class="photo" role="img" aria-label="Construction team in hard hats discussing work on site" style="background:linear-gradient(135deg,#d9d2c4,#c77c3d 55%,#5f6e7c)"></div>
    <h3>Development construction</h3>
    <p>Lorem Ipsum is simply dummy text of the printing and typesetting industry. Lorem Ipsum has.</p>
    <span class="more">LEARN MORE ›</span>
  </article>
  <article class="service-card" style="left:770px">
    <div class="photo" role="img" aria-label="Worker in safety vest renovating a building interior" style="background:linear-gradient(135deg,#e8ebee,#9aa6b0 60%,#c8d84a)"></div>
    <h3>Renovation</h3>
    <p>Lorem Ipsum is simply dummy text of the printing and typesetting industry. Lorem Ipsum has.</p>
    <span class="more">LEARN MORE ›</span>
  </article>
</section>

<section class="projects">
  <div class="projects-intro">
    <div class="eyebrow">Our Works</div>
    <h2 class="heading">Projects</h2>
    <p>Lorem Ipsum is simply dummy text of the printing and typesetting industry. Lorem Ipsum is simply dummy text of the printing and typesetting industry.</p>
    <span class="btn" style="margin-top:16px">View All Projects</span>
  </div>
  <div class="photo" role="img" aria-label="Worker in yellow hard hat on site" style="left:412px;top:1760px;width:180px;height:240px;background:linear-gradient(160deg,#4b79a8,#e7c23a 60%,#394656)"></div>
  <div class="photo" role="img" aria-label="Steel frame under construction against the sky" style="left:608px;top:1768px;width:172px;height:120px;background:linear-gradient(160deg,#8fb7d8,#5b6f84)"></div>
  <div class="photo" role="img" aria-label="Office interior with open staircase" style="left:792px;top:1760px;width:348px;height:352px;background:linear-gradient(150deg,#e6e2dc,#b07a4c 55%,#3e3a38);clip-path:polygon(0 0,92% 0,100% 8%,100% 100%,0 100%)"></div>
  <div class="photo" role="img" aria-label="Building framework with scaffolding" style="left:608px;top:1900px;width:172px;height:220px;background:linear-gradient(170deg,#cfd6dc,#6f7a84)"></div>
  <div class="photo" role="img" aria-label="Completed restaurant interior with wooden ceiling" style="left:56px;top:2032px;width:344px;height:280px;background:linear-gradient(150deg,#efe6da,#a8744a 55%,#4d3b2f);clip-path:polygon(8% 0,100% 0,100% 100%,0 100%,0 10%)"></div>
  <div class="photo" role="img" aria-label="Modern lobby interior" style="left:412px;top:2080px;width:180px;height:232px;background:linear-gradient(160deg,#f2f0ec,#b8b3aa)"></div>
  <div class="photo" role="img" aria-label="Steel structure frame" style="left:608px;top:2140px;width:172px;height:172px;background:linear-gradient(160deg,#d6e4ef,#7d8c99)"></div>
  <div class="photo" role="img" aria-label="Worker in safety vest standing on site" style="left:792px;top:2140px;width:160px;height:160px;background:linear-gradient(160deg,#b8cde0,#d7dd3c 55%,#4b5662)"></div>
</section>

<section class="contact">
  <div class="contact-copy">
    <div class="eyebrow">Contact Us</div>
    <h2 class="heading">Get In Touch With Us</h2>
    <p style="width:320px;font-size:11px;margin-bottom:16px">Lorem Ipsum is simply dummy text of the printing and typesetting industry. Lorem Ipsum is dummy.</p>
    <span class="field focus">Name *</span>
    <span class="field">Email *</span>
    <span class="field">Address *</span>
    <span class="field">Services *</span>
    <span class="field message">Message *</span>
    <span class="btn" style="margin-top:4px">Submit Message</span>
  </div>
  <svg class="abs" style="left:700px;top:2400px" width="400" height="450" viewBox="0 0 400 450"><rect x="20" y="12" width="370" height="420" fill="none" stroke="#1b8fd8" stroke-width="6"/></svg>
  <div class="photo" role="img" aria-label="Two engineers in hard hats reviewing a tablet at a construction site" style="left:710px;top:2420px;width:360px;height:420px;background:linear-gradient(160deg,#c7d8e6,#3f78b4 45%,#d9a25c 75%,#4e5b66)"></div>
  <svg class="abs" style="left:0;top:2860px" width="1200" height="180" viewBox="0 0 1200 180"><polygon points="0,0 1200,0 1200,60 600,180 0,60" fill="#f2f4f6"/></svg>
</section>

<section class="news">
  <div class="center eyebrow news-title">News</div>
  <h2 class="center heading section-title" style="top:3080px">Latest News</h2>
  <div class="photo" role="img" aria-label="Completed commercial dining interior with pendant lighting" style="left:112px;top:3180px;width:430px;height:300px;background:linear-gradient(150deg,#e9dcc6,#b07a44 50%,#4a3728)"></div>
  <article class="news-card" style="left:160px;top:3440px;width:320px;height:170px">
    <div class="news-meta"><span class="tag">Jan 5 2024</span><span>💬 3</span></div>
    <h4>Lorem Ipsum is simply dummy text of the printing and typesetting.</h4>
    <p>Lorem Ipsum is simply dummy text of the printing and typesetting industry. Lorem Ipsum has been the industry's.</p>
  </article>
  <div class="photo" role="img" aria-label="Workers in safety gear on a building site" style="left:608px;top:3180px;width:100px;height:120px;background:linear-gradient(160deg,#9bb3c8,#d6c43c 60%,#5b6570)"></div>
  <article class="news-card" style="left:690px;top:3190px;width:380px;height:110px;padding:14px 18px">
    <div class="news-meta"><span class="tag">Jan 5 2024</span><span>💬 3</span></div>
    <h4>Lorem Ipsum is simply dummy text of the printing and typesetting.</h4>
    <p>Lorem Ipsum is simply dummy text of the printing.</p>
  </article>
  <div class="photo" role="img" aria-label="Commercial kitchen counter interior" style="left:608px;top:3440px;width:100px;height:120px;background:linear-gradient(160deg,#e5e1da,#8a7d6e)"></div>
  <article class="news-card" style="left:690px;top:3450px;width:380px;height:110px;padding:14px 18px">
    <div class="news-meta"><span class="tag">Jan 5 2024</span><span>💬 3</span></div>
    <h4>Lorem Ipsum is simply dummy text of the printing and typesetting.</h4>
    <p>Lorem Ipsum is simply dummy text of the printing.</p>
  </article>
</section>

<footer class="site-footer">
  <svg class="abs" style="left:0;top:0" width="1200" height="392" viewBox="0 0 1200 392"><polygon points="0,0 1200,0 1200,30 0,110" fill="#ffffff"/><polygon points="0,110 1200,30 1200,120 0,200" fill="#1b8fd8" opacity=".12"/></svg>
  <div class="footer-col abs" style="left:60px;top:140px">
    <h5>Quick Links</h5>
    <ul><li>› Home</li><li>› About Us</li><li>› Services</li><li>› Project</li><li>› Contact Us</li></ul>
  </div>
  <div class="footer-brand">
    <div class="mark"></div>
    <div class="name">Dunmore Ridge<br>Construction</div>
  </div>
  <div class="footer-col abs" style="left:860px;top:140px;width:280px;text-align:right">
    <h5>Contact Us</h5>
    <ul class="contact-list">
      <li>142 Ridgeview Road, Dunmore<svg width="14" height="14" viewBox="0 0 14 14"><path d="M7 1a4 4 0 0 0-4 4c0 3 4 8 4 8s4-5 4-8a4 4 0 0 0-4-4z" fill="#1b8fd8"/></svg></li>
      <li>+1 555 014 2290<svg width="14" height="14" viewBox="0 0 14 14"><path d="M3 1l3 3-1.5 2a6 6 0 0 0 3.5 3.5l2-1.5 3 3-2 2C5 13 1 9 1 3z" fill="#1b8fd8"/></svg></li>
      <li>info@dunmoreridge.com<svg width="14" height="14" viewBox="0 0 14 14"><rect x="1" y="3" width="12" height="8" fill="#1b8fd8"/><path d="M1 3l6 5 6-5" stroke="#fff" fill="none"/></svg></li>
    </ul>
  </div>
  <div class="copyright">Copyright © Dunmore Ridge Construction 2024. All Rights Reserved.</div>
</footer>

</body>
</html>
```